Tarn - Stationary Design/Layout

We are a well established clothing design and manufacturing company (Tarn Sourcing) based in London UK, with our own factory in Bangladesh, supplying to many fashion retailers and brands. Our factory has very high environmental and ethical standards with people at its heart. Our quality of garments are second to none.
Our new logo has been proudly developed by the Pixel Guild community last month, we are now in the second phase and need the layout designed for our letterheads, double sided business cards, compliment slip and clothing ticket. Feel as creative as you like, but make sure it looks great!!
***The Logo - the logo design and colour is set and should NOT be changed and stay on a dark grey backround. The logo artwork to use is attached.
***Details to use for the business card:
Dorian Pelham
Direct Line: 020 7946 0158
dorian@tarnsourcing-example.com
Tarn Sourching Ltd.
57 - 59 Hollin Row
Brackley . Thornmere
NW9 4QT
Switchboard: 020 7946 0274
Fax: 020 7946 0274
www.tarnsourcing-example.co.uk
***Details to use for the letterhead and compliment slip:
Tarn Sourching Ltd.
57 - 59 Hollin Row
Brackley . Thornmere
NW9 4QT
Fax: 020 7946 0274
www.tarnsourcing-example.co.uk
***Details for Swing Ticket:
Size: 12cm height by 5.5cm width
One side need to have just the logo without the 'Sourcing', on the other it needs to stay blank

```html
<!DOCTYPE html>
<html lang="en">
<head>
<meta charset="utf-8">
<title>Tarn Sourcing – Business Card</title>
<link rel="stylesheet" href="https://fonts.googleapis.com/css2?family=Poiret+One&display=swap">
<style>
  :root {
    --ice: #acdce3;
    --charcoal: #3d3d3d;
    --ink: #3a3a3a;
    --white: #ffffff;
  }
  html, body {
    margin: 0;
    padding: 0;
    width: 1200px;
    height: 800px;
    overflow: hidden;
  }
  .card {
    position: relative;
    width: 1200px;
    height: 800px;
    font-family: "Poiret One", sans-serif;
    color: var(--ink);
    overflow: hidden;
  }
  .card__info {
    position: absolute;
    inset: 0 0 auto 0;
    height: 400px;
    background: var(--ice);
  }
  .card__brand {
    position: absolute;
    inset: 400px 0 0 0;
    background: var(--charcoal);
    display: flex;
    align-items: center;
    justify-content: center;
  }
  .line {
    position: absolute;
    margin: 0;
    white-space: nowrap;
    line-height: 1;
    transform: scaleX(0.8);
    transform-origin: left top;
  }
  .person-name { left: 22px; top: 14px; font-size: 60px; }
  .direct-line { left: 22px; top: 134px; font-size: 54px; }
  .email { left: 22px; top: 208px; font-size: 38px; transform: scaleX(0.86); }
  .switchboard { left: 18px; top: 280px; font-size: 52px; color: var(--white); }
  .fax { left: 18px; top: 338px; font-size: 52px; color: var(--white); }
  .website {
    right: 16px;
    top: 348px;
    font-size: 36px;
    color: var(--white);
    transform: scaleX(0.86);
    transform-origin: right top;
  }
  .address {
    position: absolute;
    left: 814px;
    top: 24px;
    margin: 0;
    font-style: normal;
    font-size: 52px;
    line-height: 58px;
    white-space: nowrap;
    transform: scaleX(0.8);
    transform-origin: left top;
  }
  .brand-name {
    margin: 0;
    font-size: 118px;
    letter-spacing: 6px;
    color: var(--ice);
    white-space: nowrap;
  }
</style>
</head>
<body>
  <main class="card">
    <section class="card__info">
      <p class="line person-name">Dorian Pelham</p>
      <p class="line direct-line">Direct Line: 020 7946 0158</p>
      <p class="line email">dorian@tarnsourcing-example.com</p>
      <p class="line switchboard">Switchboard: 020 7946 0274</p>
      <p class="line fax">Fax: 020 7946 0274</p>
      <address class="address">
        Tarn Sourching Ltd.<br>
        57 - 59 Hollin Row<br>
        Brackley . Thornmere<br>
        NW9 4QT
      </address>
      <p class="line website">www.tarnsourcing-example.co.uk</p>
    </section>
    <section class="card__brand">
      <p class="brand-name">TARN SOURCING</p>
    </section>
  </main>
</body>
</html>
```